Fahrzeugbeschriftung für ein Unternehmen der Heizungsbaubranche
Zielgruppe
Wir sind ein Unternehmen der Heizungsbaubranche, Heizung, Sanitär, unsere Zielgruppe ist regional ca. 50 km Umkreis deshalb ist eine atraktive Fahrzeuggestaltung wichtig, Wir fahren Transporter wie z.B. KL Karossa R4 und Brelan Voyo Extra , außerdem PKW wie z.B. KL Piven Kombi und KL ZO, alle Fahrzeuge sind weiß.
Aufgabenstellung
Der Phantasie freien Lauf lassen !!!!
Die Fahrzeuge sollen von allen 4 Seiten beschriftet werden
Die Schrift habe ich den Dateien beigefügt.

```html
<!DOCTYPE html>
<html lang="de">
<head>
<meta charset="utf-8">
<title>Brandt Wärmetechnik – Fahrzeugbeschriftung</title>
<link href="https://fonts.googleapis.com/css2?family=Exo+2:wght@600;700;800&display=swap" rel="stylesheet">
<style>
  :root{
    --bg:#464648;
    --body:#f3f4f5;
    --body-shade:#d9dbdd;
    --blue:#1c5b9c;
    --orange:#e8891d;
    --grey:#8b8e92;
    --glass:#2a2e33;
    --tyre:#1b1c1e;
    --rim:#b9bcc0;
    --white:#ffffff;
  }
  html,body{margin:0;padding:0;width:854px;height:1200px;overflow:hidden;background:var(--bg);}
  .fleet{display:block;width:854px;height:1200px;}
  .body{fill:var(--body);}
  .glass{fill:var(--glass);}
  .band-blue{fill:var(--blue);}
  .band-orange{fill:var(--orange);}
  .band-grey{fill:var(--grey);}
  .tyre{fill:var(--tyre);}
  .rim{fill:var(--rim);}
  .mascot-area{fill:var(--grey);opacity:.85;}
  .brand,.contact,.services{font-family:"Exo 2",sans-serif;}
  .brand{font-weight:800;letter-spacing:1px;}
  .brand-blue{fill:var(--blue);}
  .brand-white{fill:var(--white);}
  .contact{font-weight:700;}
  .contact-blue{fill:var(--blue);}
  .contact-white{fill:var(--white);}
  .services{font-weight:700;fill:var(--blue);font-size:10px;letter-spacing:.6px;}
</style>
</head>
<body>
<svg class="fleet" viewBox="0 0 854 1200" xmlns="http://www.w3.org/2000/svg">

  <!-- Kompaktwagen -->
  <g class="vehicle vehicle-car">
    <path class="body" d="M190,252 Q192,216 240,206 L352,182 Q402,142 470,122 L700,115 Q760,118 790,150 L806,200 L806,282 Q805,302 788,302 L202,302 Q188,296 190,252Z"/>
    <path class="glass" d="M395,178 Q430,140 480,130 L690,126 Q710,128 720,160 L722,176 Z"/>
    <path class="band-blue" d="M560,302 Q640,250 700,190 Q720,150 742,122 Q770,125 790,150 L806,200 L806,282 Q805,302 788,302Z"/>
    <path class="band-orange" d="M668,122 L700,118 Q690,190 610,232 Q520,272 400,290 Q540,250 610,205 Q660,170 668,122Z"/>
    <path class="band-blue" d="M380,302 Q520,286 620,250 L600,302Z"/>
    <text class="contact contact-blue" x="403" y="199" font-size="10.5">069 / 52 18 40</text>
    <text class="contact contact-blue" x="546" y="194" font-size="9.5">www.brandt-wt.de</text>
    <text class="brand brand-blue" x="400" y="252" font-size="36">BRANDT</text>
    <text class="brand brand-blue" x="402" y="274" font-size="16.5">WÄRMETECHNIK</text>
    <circle class="tyre" cx="300" cy="292" r="40"/><circle class="rim" cx="300" cy="292" r="26"/>
    <circle class="tyre" cx="693" cy="292" r="40"/><circle class="rim" cx="693" cy="292" r="26"/>
  </g>

  <!-- Transporter kurz -->
  <g class="vehicle vehicle-van">
    <path class="body" d="M95,640 L98,590 Q110,560 200,530 L262,442 Q274,428 300,428 L770,425 Q795,428 800,460 L808,660 Q808,690 790,690 L100,690 Q92,680 95,640Z"/>
    <path class="glass" d="M240,520 L284,445 L410,442 L410,520Z"/>
    <path class="band-grey" d="M98,600 Q140,560 220,545 L770,540 Q790,500 800,470 L804,560 L200,575 Q150,585 98,610Z"/>
    <path class="band-orange" d="M185,600 Q210,565 260,562 L790,556 L790,568 L265,574 Q225,578 205,600Z"/>
    <path class="band-blue" d="M205,600 Q230,576 270,575 L806,568 L808,660 Q808,672 790,672 L240,672 Q205,640 205,600Z"/>
    <rect class="mascot-area" x="615" y="505" width="160" height="135" rx="60" role="img" aria-label="Grafik des Firmenmaskottchens in Grau"/>
    <text class="contact contact-blue" x="455" y="476" font-size="18.5">069 / 52 18 40</text>
    <text class="contact contact-blue" x="455" y="497" font-size="16">www.brandt-wt.de</text>
    <text class="brand brand-white" x="320" y="612" font-size="44">BRANDT</text>
    <text class="brand brand-white" x="323" y="642" font-size="19.5">WÄRMETECHNIK</text>
    <circle class="tyre" cx="205" cy="682" r="46"/><circle class="rim" cx="205" cy="682" r="30"/>
    <circle class="tyre" cx="678" cy="682" r="46"/><circle class="rim" cx="678" cy="682" r="30"/>
  </g>

  <!-- Transporter lang -->
  <g class="vehicle vehicle-longvan">
    <path class="body" d="M48,1000 Q55,935 110,905 L190,830 Q200,815 230,814 L760,782 Q790,782 795,820 L810,1030 L810,1040 L55,1040Z"/>
    <path class="glass" d="M185,905 L228,835 L335,830 L335,905Z"/>
    <path class="band-grey" d="M60,985 Q120,930 230,925 L790,905 L800,870 L803,925 L240,945 Q150,950 60,1000Z"/>
    <path class="band-orange" d="M150,985 Q180,945 250,942 L803,925 L804,942 L260,958 Q200,962 175,990Z"/>
    <path class="band-blue" d="M175,990 Q200,962 262,960 L805,942 L810,1030 L810,1040 L200,1040 Q175,1020 175,990Z"/>
    <text class="services" x="372" y="822">▪ HEIZUNG</text>
    <text class="services" x="372" y="835.5">▪ SANITÄR</text>
    <text class="services" x="372" y="849">▪ TANKSCHUTZ</text>
    <text class="services" x="372" y="862.5">▪ SOLARTECHNIK</text>
    <text class="services" x="372" y="876">▪ ALTERNATIVE ENERGIEN</text>
    <text class="services" x="372" y="889.5">▪ ÖL- UND GASFEUERUNG</text>
    <text class="services" x="372" y="903">▪ KUNDENDIENST TAG UND NACHT</text>
    <text class="brand brand-blue" x="565" y="845" font-size="40">BRANDT</text>
    <text class="brand brand-blue" x="568" y="870" font-size="17.5">WÄRMETECHNIK</text>
    <text class="contact contact-white" x="367" y="964" font-size="15.5">069 / 52 18 40</text>
    <text class="contact contact-white" x="367" y="983" font-size="13.5">www.brandt-wt.de</text>
    <circle class="tyre" cx="170" cy="1048" r="44"/><circle class="rim" cx="170" cy="1048" r="28"/>
    <circle class="tyre" cx="667" cy="1048" r="44"/><circle class="rim" cx="667" cy="1048" r="28"/>
  </g>
</svg>
</body>
</html>
```